New Business Card Design Project VORASTI-Italy

we are VORASTI-Italy
our company in the market for 3 years we are luxury cosmetic company and its about time for a facelift :)
i will like to have elegant luxurious and unique business card
that will give the person that get it a unique, luxurious and elegant impression
I'm VERY OPEN FOR NEW IDEAS , even duo i add a few files of things that i see on line and i like them

i add my logo as well
my website is VORASTI.COM
(if you would like to see the main style that we have)

Target Market(s)

adult that have money :)

Industry/Entity Type

Business

Contact Information for Business Card

Name - Paul Vorasti
Position - CEO and CO Founder
address - 4817 E Larkdale
telephone - 555-384-1962
email - paul@vorasti.com
fax - 555-384-1962
website - VORASTI.COM

Colors
000000
959595
fbee3e
ffffff

Requirements
Must have
• big logo in GOLD color
• elegant look
• impressive
Nice to have
• not must but maybe classy pattern background
• not must but maybe emblem
• maybe clear plastic business card
Should not have
• colors
• images

```html
<!DOCTYPE html>
<html lang="en">
<head>
<meta charset="utf-8">
<title>VORASTI Italy – Business Card</title>
<link rel="stylesheet" href="https://fonts.googleapis.com/css2?family=Open+Sans:wght@400;600;700&display=swap">
<style>
  :root {
    --black: #000000;
    --ink: #0d0d0d;
    --gold: #d6a21e;
    --gold-text: #c9a233;
    --white: #ffffff;
    --grey: #c8c8c8;
    --stage: #ecefe4;
  }
  * { margin: 0; padding: 0; box-sizing: border-box; }
  html, body { width: 1200px; height: 835px; overflow: hidden; }
  body {
    background: var(--stage);
    font-family: "Open Sans", Arial, sans-serif;
    position: relative;
  }
  .card {
    position: absolute;
    top: 268px;
    width: 520px;
    height: 300px;
    overflow: hidden;
    box-shadow: 0 10px 30px rgba(0,0,0,.18);
  }
  .card--front { left: 50px; background: var(--black); }
  .card--back { left: 630px; background: var(--ink); }

  /* Brand name placeholder: one colour, one weight, one plain circle */
  .brand {
    position: absolute; left: 0; right: 0;
    display: flex; flex-direction: column; align-items: center;
    color: var(--gold-text);
  }
  .brand__circle { border: 2px solid var(--gold-text); border-radius: 50%; }
  .brand__name {
    font-family: "Open Sans", Arial, sans-serif;
    font-weight: 600;
    line-height: 1.1;
    white-space: nowrap;
  }
  .card--front .brand { top: 58px; }
  .card--front .brand__circle { width: 112px; height: 112px; margin-bottom: 22px; }
  .card--front .brand__name { font-size: 52px; }

  /* Back card */
  .side-panel {
    position: absolute; top: 0; right: 0; width: 160px; height: 100%;
    background: var(--white);
    border-left: 6px solid var(--grey);
  }
  .side-panel .brand { top: 88px; }
  .side-panel .brand__circle { width: 66px; height: 66px; margin-bottom: 12px; }
  .side-panel .brand__name { font-size: 17px; }

  .identity { position: absolute; left: 44px; top: 24px; color: var(--gold-text); }
  .identity__name { font-size: 30px; font-weight: 700; line-height: 1.1; }
  .identity__role { font-size: 10px; font-weight: 600; color: var(--white); margin-top: 2px; }

  .contact-band {
    position: absolute; left: 0; width: 354px;
    background: var(--gold);
    display: flex;
  }
  .contact-band--phone { top: 98px; height: 66px; }
  .contact-band--web { top: 172px; height: 62px; }
  .contact-band--address { top: 242px; height: 58px; }
  .contact-band__icons {
    width: 40px; background: var(--white);
    display: flex; flex-direction: column; justify-content: center; align-items: center; gap: 8px;
  }
  .contact-band__icons svg { width: 16px; height: 16px; fill: var(--black); }
  .contact-band__lines {
    padding-left: 18px;
    display: flex; flex-direction: column; justify-content: center;
    font-size: 18px; color: var(--black); line-height: 1.3;
  }
  .contact-band--address .contact-band__lines { font-size: 21px; }
</style>
</head>
<body>

  <section class="card card--front" aria-label="Business card front">
    <div class="brand">
      <div class="brand__circle"></div>
      <div class="brand__name">VORASTI Italy</div>
    </div>
  </section>

  <section class="card card--back" aria-label="Business card back">
    <div class="identity">
      <div class="identity__name">Paul Vorasti</div>
      <div class="identity__role">CEO &amp; CO Founder</div>
    </div>

    <div class="contact-band contact-band--phone">
      <div class="contact-band__icons">
        <svg viewBox="0 0 24 24" aria-label="Phone"><path d="M6.6 10.8a15.1 15.1 0 0 0 6.6 6.6l2.2-2.2c.3-.3.7-.4 1-.2 1.1.4 2.3.6 3.6.6.6 0 1 .4 1 1V20c0 .6-.4 1-1 1A17 17 0 0 1 3 4c0-.6.4-1 1-1h3.5c.6 0 1 .4 1 1 0 1.3.2 2.5.6 3.6.1.3 0 .7-.2 1z"/></svg>
        <svg viewBox="0 0 24 24" aria-label="Fax"><path d="M6 2h12v5H6zM3 8h18a1 1 0 0 1 1 1v8h-4v5H6v-5H2V9a1 1 0 0 1 1-1zm5 7v5h8v-5z"/></svg>
      </div>
      <div class="contact-band__lines">
        <span>555-384-1962</span>
        <span>555-384-1962</span>
      </div>
    </div>

    <div class="contact-band contact-band--web">
      <div class="contact-band__icons">
        <svg viewBox="0 0 24 24" aria-label="Email"><path d="M2 5h20v14H2zm2 2v.5l8 5.5 8-5.5V7z"/></svg>
        <svg viewBox="0 0 24 24" aria-label="Website"><circle cx="12" cy="12" r="10"/></svg>
      </div>
      <div class="contact-band__lines">
        <span>paul@vorasti.com</span>
        <span>www.vorasti.com</span>
      </div>
    </div>

    <div class="contact-band contact-band--address">
      <div class="contact-band__icons">
        <svg viewBox="0 0 24 24" aria-label="Address"><path d="M12 2a7 7 0 0 0-7 7c0 5 7 13 7 13s7-8 7-13a7 7 0 0 0-7-7zm0 9.5A2.5 2.5 0 1 1 12 6.5a2.5 2.5 0 0 1 0 5z"/></svg>
      </div>
      <div class="contact-band__lines">
        <span>4817 E Larkdale</span>
      </div>
    </div>

    <div class="side-panel">
      <div class="brand">
        <div class="brand__circle"></div>
        <div class="brand__name">VORASTI Italy</div>
      </div>
    </div>
  </section>

</body>
</html>
```